Consumer Credit Attorney Needs Logo for Letterhead & Business cards

I need a basic logo or letterhead design for a new law firm in Mobile, Alabama. The firm is called "Marlow T. Fenwick, PC." We represent people fighting large corporations in cases involving Fair Credit Reporting, Debt Collection, Mortgage Fraud, Truth in Lending, and Wrongful Foreclosures. I don't want anything with scales of justice or columns or the typical lawyer imagery. I ride a bike to court. I keep most of my office in the cloud. I'm a different type of lawyer, and I want a design that is simple, elegant, and made primarily of blue and white.

The Job is now Payment Committed.  I look forward to seeing your submissions.  Thanks1

Reason: I have just recently received some new designs and provided feedback on them. You all deserve some time to consider the feedback. Thanks!

• Clear lines and a small footprint on the letterhead. I like several antique styles- Gilded Age, Rococo, Edwardian, even Art Deco.
• The only thing I hate is 1990s clip-art style graphics. No illustrations of money, courthouses, scales, columns, etc. I also hate silly fonts, overly fancy or "handwritten" fonts, and Arial font.

```html
<!DOCTYPE html>
<html lang="en">
<head>
<meta charset="utf-8">
<title>Marlow T. Fenwick, P.C. — Letterhead</title>
<link rel="stylesheet" href="https://fonts.googleapis.com/css2?family=Source+Sans+3:wght@300;400&display=swap">
<style>
  :root {
    --ink-blue: #1f32c4;
    --sage: #d6e0ae;
    --sage-pale: #edf1da;
    --paper: #ffffff;
  }
  * { margin: 0; padding: 0; box-sizing: border-box; }
  html, body {
    width: 927px;
    height: 1200px;
    overflow: hidden;
    background: var(--paper);
  }
  .letterhead {
    position: relative;
    width: 927px;
    height: 1200px;
    overflow: hidden;
    background: var(--paper);
    font-family: "Source Sans 3", sans-serif;
    color: var(--ink-blue);
  }
  .firm-heading {
    position: absolute;
    left: 37px;
    top: 44px;
  }
  .firm-heading__lead {
    display: block;
    font-weight: 300;
    font-size: 20px;
    line-height: 24px;
  }
  .firm-heading__name {
    display: block;
    font-weight: 300;
    font-size: 36px;
    line-height: 42px;
    margin-top: 4px;
    letter-spacing: 0.2px;
  }
  .firm-mark {
    position: absolute;
    right: 52px;
    top: 62px;
    font-weight: 400;
    font-size: 54px;
    color: var(--sage);
    letter-spacing: 1px;
  }
  .skyline-art {
    position: absolute;
    left: 0;
    bottom: 0;
    width: 927px;
    height: 510px;
    background: linear-gradient(to bottom,
      rgba(237, 241, 218, 0) 0%,
      var(--sage-pale) 22%,
      var(--sage-pale) 100%);
  }
  .contact-block {
    position: absolute;
    left: 31px;
    top: 1050px;
    font-weight: 400;
    font-size: 21px;
    line-height: 29.5px;
  }
</style>
</head>
<body>
  <main class="letterhead">
    <header class="firm-heading">
      <span class="firm-heading__lead">The Law Office of</span>
      <span class="firm-heading__name">Marlow T. Fenwick, P.C.</span>
    </header>

    <div class="firm-mark">Fenwick</div>

    <div class="skyline-art" role="img" aria-label="Faint pale green silhouette of a downtown Mobile waterfront building with an arched steel canopy and a flag"></div>

    <address class="contact-block" style="font-style: normal;">
      <div>412 Harbor Lane</div>
      <div>Mobile, Alabama 36602</div>
      <div>251.555.0142</div>
      <div>office@fenwicklaw.example</div>
    </address>
  </main>
</body>
</html>
```